Auto electrical business that is mobile so we come to you so it doesn't matter if the car, 4wd, cara

We need a business card designed that will capture people's attention. We are based in Bathurst & we are a Mobile Auto Electrical business that works on cars, 4dw's, caravans, trucks, farming equipment through to mining equipment

```html
<!DOCTYPE html>
<html lang="en">
<head>
<meta charset="utf-8">
<title>Reid's Mobile Auto Electrical – Business Card</title>
<link rel="stylesheet" href="https://fonts.googleapis.com/css2?family=Archivo:wght@700;800;900&display=swap">
<style>
  :root {
    --page: #ffffff;
    --stage: #cacaca;
    --card-yellow: #eec41e;
    --ink: #1d1a17;
    --accent: #f0c419;
    --field-dark: #120d09;
    --field-mid: #4a3420;
    --field-warm: #8a6238;
    --crop-green: #3f6a2a;
  }
  * { margin: 0; padding: 0; box-sizing: border-box; }
  html, body { width: 1200px; height: 1000px; overflow: hidden; background: var(--page); }
  body { font-family: "Archivo", Arial, sans-serif; position: relative; }

  .stage { position: absolute; left: 90px; top: 0; width: 1020px; height: 1000px; background: var(--stage); }

  .card {
    position: absolute; left: 320px; width: 560px; height: 343px;
    box-shadow: 4px 5px 7px rgba(0,0,0,.35);
    text-align: center; overflow: hidden;
  }
  .card--front { top: 130px; background: var(--card-yellow); color: var(--ink); }
  .card--back { top: 554px; color: var(--accent); }

  .brand { position: absolute; left: 0; right: 0; }
  .brand__name {
    display: inline-flex; align-items: center; gap: 14px;
    font-weight: 900; font-size: 70px; line-height: 1; letter-spacing: 1px;
  }
  .brand__mark { width: 26px; height: 26px; background: currentColor; }
  .brand__tagline { font-weight: 900; font-size: 22px; margin-top: 6px; letter-spacing: .5px; }

  .card--front .brand { top: 92px; }
  .card--back .brand { top: 24px; }

  .contact { position: absolute; left: 0; right: 0; top: 212px; font-weight: 800; }
  .contact__label { font-size: 18px; letter-spacing: .5px; }
  .contact__phone { font-size: 24px; margin-top: 2px; letter-spacing: .5px; }
  .contact__email { font-size: 17px; margin-top: 6px; }

  .card__photo {
    position: absolute; inset: 0;
    background:
      radial-gradient(ellipse 40% 35% at 68% 38%, var(--crop-green) 0%, transparent 70%),
      radial-gradient(ellipse 70% 55% at 55% 35%, var(--field-warm) 0%, transparent 75%),
      linear-gradient(180deg, var(--field-dark) 0%, var(--field-mid) 45%, var(--field-dark) 100%);
  }
  .card__photo::after { content: ""; position: absolute; inset: 0; background: rgba(0,0,0,.15); }

  .services {
    position: absolute; left: 20px; right: 20px; top: 142px;
    font-weight: 800; font-size: 21px; line-height: 27px; letter-spacing: 1.4px;
  }
  .back-phone {
    position: absolute; left: 0; right: 0; top: 298px;
    font-weight: 800; font-size: 24px; letter-spacing: .6px;
  }
</style>
</head>
<body>
  <div class="stage"></div>

  <section class="card card--front">
    <div class="brand">
      <div class="brand__name"><span class="brand__mark"></span>Reid's</div>
      <div class="brand__tagline">Mobile Auto Electrical</div>
    </div>
    <div class="contact">
      <div class="contact__label">PHONE</div>
      <div class="contact__phone">0400 00SPARK / 0400 007727</div>
      <div class="contact__email">reidsmobile@example.com</div>
    </div>
  </section>

  <section class="card card--back">
    <div class="card__photo" role="img" aria-label="Photo of a tractor working a ploughed field at dusk with headlights on"></div>
    <div class="brand">
      <div class="brand__name"><span class="brand__mark"></span>Reid's</div>
      <div class="brand__tagline">Mobile Auto Electrical</div>
    </div>
    <p class="services">ALL FARMING AND PLANT EQUIPAMENT, AIR-CON NEEDS, LIGHT AND HEAVY VEHICLE, CARA-<br>VAN AND CAMPING<br>SYSTEMS.</p>
    <p class="back-phone">PHONE 0400 00SPARK / 0400007727</p>
  </section>
</body>
</html>
```